Metal Pail and Round Tin Can Design for Resin Manufacturer

We are a fbreglass resin manufacturer located in Australia. We manufacturer resins. We are looking to have custom printed pails and can s made. We would like a innovative, and fresh design to be printed on our packaging. We would like the colours blue and white incorporated in the design. We want to show that we are a professional company with a modern touch on chemical manufacturing. Some design work will need to leave space for compliance labeling, similar to paint cans that are in many shops. Use professional paint can/pail designs as inspiration, incorporating in our current logos and design.

Target Market(s)

Fibreglass Resin Market, Fibreglass Manufacturing, Coatings

Font styles to use
Sans Serif

Colors

Designer to choose colors to be used in the design.

Requirements
Must have
• Compliance, safety information, quality ISO 9001 certification.
• The design will need to be able to be printed on several different sized cans. We would like the same consistent design on the 3 types of cans, the only changes would be the size of the product label that we would attach.
• I have attached the safety information that must be on the label. The font can be changed to match the design.
• Our 2 logos must be present on the can.
Nice to have
• A designated area to put our plain white product label. Dimension attached below.

```html
<!DOCTYPE html>
<html lang="en">
<head>
<meta charset="utf-8">
<title>Corvan Composites – Pail Label</title>
<link href="https://fonts.googleapis.com/css2?family=Barlow+Condensed:wght@400;500;600;700;800&display=swap" rel="stylesheet">
<style>
  :root{
    --navy:#252c8c;
    --navy-deep:#1b2170;
    --blue:#2f57d8;
    --cyan:#3fb8ec;
    --sky:#9fdcf7;
    --white:#ffffff;
    --mist:#eef1f6;
    --red:#d3252f;
    --orange:#e27a22;
    --orange-dark:#b9561a;
    --grey:#5a5e6a;
    --ink:#2a2d3a;
  }
  *{box-sizing:border-box;margin:0;padding:0}
  html,body{width:1200px;height:640px;overflow:hidden}
  body{background:var(--white);font-family:"Barlow Condensed",sans-serif;color:var(--ink);position:relative}
  .label{position:absolute;top:40px;width:540px;height:560px;overflow:hidden;border-radius:6px;box-shadow:0 0 0 1px #dde2ea}
  .label--front{left:40px}
  .label--back{left:620px}
  .label__art{position:absolute;inset:0;width:100%;height:100%}
  .brand{position:absolute;display:flex;align-items:center;gap:14px;color:var(--navy);font-weight:800;text-transform:uppercase;letter-spacing:2px;line-height:.95}
  .brand__dot{width:22px;height:22px;border-radius:50%;background:var(--red);flex:none}
  .label--front .brand{left:0;right:0;top:110px;justify-content:center;font-size:62px}
  .label--back .brand{right:30px;top:56px;font-size:24px;gap:8px;letter-spacing:1px}
  .label--back .brand__dot{width:12px;height:12px}
  .steps{position:absolute;inset:0}
  .step{position:absolute;width:80px;text-align:center}
  .step__icon{display:block;width:70px;height:70px;margin:0 auto 6px;border-radius:50%;background:radial-gradient(circle at 40% 35%,#f39a43,var(--orange) 55%,var(--orange-dark));border:3px solid #f4f4f4;box-shadow:0 2px 4px rgba(0,0,0,.25)}
  .step__name{font-size:15px;font-weight:600;color:var(--white);letter-spacing:1px}
  .step--mix .step__name{color:var(--sky)}
  .cert-badge{position:absolute;left:24px;top:440px;width:66px;height:90px}
  .volume{position:absolute;left:232px;top:498px;border:2px solid var(--white);border-radius:6px;padding:0 10px;font-size:36px;font-weight:500;color:var(--white);line-height:1.1}

  .safety{position:absolute;left:40px;top:40px;width:300px}
  .safety__title{font-size:24px;font-weight:700;color:var(--red);letter-spacing:.3px;line-height:29px}
  .safety__sub{font-size:14px;font-weight:600;color:var(--blue);margin-top:6px;line-height:17px}
  .safety__list{list-style:none;font-size:11px;line-height:13px;color:var(--ink)}
  .safety__list li::before{content:"•"}
  .handling{position:absolute;left:32px;top:186px;width:320px;padding:6px 8px 8px;background:rgba(255,255,255,.78);border-radius:3px}
  .handling .safety__sub{margin-top:0}
  .handling .safety__list{font-size:10px;line-height:12px}
  .sds-note{position:absolute;right:30px;top:124px;width:140px;text-align:center;font-size:11px;color:var(--navy);line-height:1.25;text-transform:uppercase}
  .child-warning{position:absolute;right:28px;top:260px;width:150px;text-align:center;font-size:12px;color:var(--red);text-transform:uppercase;font-weight:500}
  .child-warning svg{display:block;margin:6px auto 0}
  .first-aid{position:absolute;left:32px;top:446px;width:320px;color:var(--white)}
  .first-aid__title{font-size:14px;font-weight:600;line-height:17px}
  .first-aid .safety__list{color:var(--white);font-size:9.5px;line-height:11.5px}
  .quality-badge{position:absolute;right:34px;top:426px;width:110px;height:36px}
  .contact{position:absolute;right:22px;top:478px;width:150px;padding:6px 8px;border:1px dashed var(--white);border-radius:4px;color:var(--white);font-size:9px;line-height:12px}
  .contact__name{font-size:12px;font-weight:600;text-decoration:underline}
</style>
</head>
<body>

<section class="label label--front">
  <svg class="label__art" viewBox="0 0 540 560" preserveAspectRatio="none" aria-hidden="true">
    <defs>
      <linearGradient id="frontBase" x1="0" y1="0" x2="0" y2="1">
        <stop offset="0" stop-color="#ffffff"/><stop offset="1" stop-color="#e4e8ee"/>
      </linearGradient>
      <linearGradient id="frontNavy" x1="0" y1="0" x2="1" y2="1">
        <stop offset="0" stop-color="#2b3fb8"/><stop offset="1" stop-color="#1b2170"/>
      </linearGradient>
      <linearGradient id="frontBlob" x1="0" y1="0" x2="1" y2="1">
        <stop offset="0" stop-color="#2f57d8"/><stop offset="1" stop-color="#9fdcf7"/>
      </linearGradient>
    </defs>
    <rect width="540" height="560" fill="url(#frontBase)"/>
    <path d="M470,0 H540 V560 H500 C520,420 540,300 500,250 C460,200 520,120 470,0Z" fill="#2f57d8"/>
    <path d="M540,160 C470,240 380,260 370,330 C360,380 440,390 540,370Z" fill="url(#frontBlob)"/>
    <ellipse cx="468" cy="380" rx="30" ry="48" fill="#3f7fe4"/>
    <circle cx="504" cy="430" r="9" fill="#2f57d8"/>
    <path d="M0,200 C90,300 200,360 330,380 C430,395 500,420 540,470 V560 H0Z" fill="#3fb8ec"/>
    <path d="M0,240 C90,340 220,410 360,430 C450,442 510,460 540,500 V560 H0Z" fill="url(#frontNavy)"/>
    <path d="M0,400 C150,470 330,450 540,520 V540 C330,470 150,490 0,430Z" fill="#5ccaf2" opacity=".85"/>
  </svg>

  <div class="brand"><span class="brand__dot"></span><span>Corvan<br>Composites</span></div>

  <div class="steps">
    <div class="step step--mix" style="left:22px;top:250px"><span class="step__icon" role="img" aria-label="Mixing icon"></span><span class="step__name">MIX</span></div>
    <div class="step" style="left:106px;top:300px"><span class="step__icon" role="img" aria-label="Pouring icon"></span><span class="step__name">POUR</span></div>
    <div class="step" style="left:186px;top:342px"><span class="step__icon" role="img" aria-label="Spreading icon"></span><span class="step__name">SPREAD</span></div>
    <div class="step" style="left:272px;top:364px"><span class="step__icon" role="img" aria-label="Rolling icon"></span><span class="step__name">ROLL</span></div>
  </div>

  <svg class="cert-badge" viewBox="0 0 66 90" aria-hidden="true">
    <path d="M33,2 L64,14 V52 C64,70 50,82 33,88 C16,82 2,70 2,52 V14Z" fill="var(--orange)" stroke="#4a4d58" stroke-width="3"/>
  </svg>

  <div class="volume">20L</div>
</section>

<section class="label label--back">
  <svg class="label__art" viewBox="0 0 540 560" preserveAspectRatio="none" aria-hidden="true">
    <defs>
      <linearGradient id="backBase" x1="0" y1="0" x2="0" y2="1">
        <stop offset="0" stop-color="#ffffff"/><stop offset="1" stop-color="#e4e8ee"/>
      </linearGradient>
      <linearGradient id="backNavy" x1="0" y1="0" x2="1" y2="1">
        <stop offset="0" stop-color="#2b3fb8"/><stop offset="1" stop-color="#1b2170"/>
      </linearGradient>
    </defs>
    <rect width="540" height="560" fill="url(#backBase)"/>
    <path d="M0,0 H30 C20,60 50,120 30,170 C15,210 10,220 0,240Z" fill="#2f57d8"/>
    <path d="M540,180 C470,260 420,300 360,330 C320,350 330,380 400,370 C460,360 520,300 540,280Z" fill="#c9cdf0" opacity=".7"/>
    <path d="M0,440 C150,400 330,340 540,220 V560 H0Z" fill="#3fb8ec"/>
    <path d="M0,470 C170,430 340,380 540,300 V560 H0Z" fill="url(#backNavy)"/>
    <path d="M0,520 C180,480 360,470 540,430 V444 C360,486 180,496 0,536Z" fill="#5ccaf2" opacity=".7"/>
  </svg>

  <div class="safety">
    <h2 class="safety__title">SAFETY, HANDLING AND STORAGE</h2>
    <h3 class="safety__sub">Precautions for Storage:</h3>
    <ul class="safety__list">
      <li>Store away from incompatible materials. Refer to SDS.</li>
      <li>Store locked up.</li>
      <li>Store in a cool, dry place away from direct sunlight.</li>
      <li>Do not pressurize, cut, heat or weld containers - residual vapours may be flammable.</li>
      <li>This product may be flammable and will fuel a fire in progress.</li>
    </ul>
  </div>

  <div class="handling">
    <h3 class="safety__sub">Precautions for Handling:</h3>
    <ul class="safety__list">
      <li>Keep out of reach of children.</li>
      <li>Read label before use.</li>
      <li>Obtain special instructions before use.</li>
      <li>Do not handle until all safety precautions have been read and understood.</li>
      <li>Keep away from heat, sparks, open flames or hot surfaces. No smoking.</li>
      <li>Keep container tightly closed.</li>
      <li>Ground, bond container and receiving equipment.</li>
      <li>Use explosion-proof electrical, ventilating and lighting.</li>
      <li>Use only non-sparking tools.</li>
      <li>Take precautionary measures against static discharge.</li>
      <li>Open slowly to control possible pressure release.</li>
      <li>Do not breathe fumes, vapours or spray.</li>
      <li>Wash hands thoroughly after handling.</li>
      <li>Do not eat, drink or smoke when using this product.</li>
      <li>Avoid release to the environment.</li>
      <li>Wear protective clothing.</li>
      <li>Use personal protective equipment as required.</li>
    </ul>
  </div>

  <div class="brand"><span class="brand__dot"></span><span>Corvan<br>Composites</span></div>
  <p class="sds-note">Always refer to the product safety data sheet before use</p>

  <div class="child-warning">
    Keep out of reach of children
    <svg width="40" height="40" viewBox="0 0 40 40" aria-hidden="true">
      <circle cx="20" cy="20" r="17" fill="none" stroke="var(--red)" stroke-width="3"/>
      <line x1="8" y1="8" x2="32" y2="32" stroke="var(--red)" stroke-width="3"/>
    </svg>
  </div>

  <div class="first-aid">
    <h3 class="first-aid__title">First Aid</h3>
    <ul class="safety__list">
      <li>If swallowed DO NOT induce vomiting, rinse mouth with water and give a glass of water or milk.</li>
      <li>If vomiting occurs, keep patients head down to prevent vomit entering lungs.</li>
      <li>If splashed in eyes, flood with low pressure water for at least 15 minutes.</li>
      <li>If splashed on skin remove contaminated clothing and gently wash skin with mild soap and water.</li>
      <li>If irritating or swelling occurs, seek medical attention.</li>
    </ul>
  </div>

  <svg class="quality-badge" viewBox="0 0 110 36" aria-hidden="true">
    <rect x="1" y="1" width="108" height="34" rx="17" fill="var(--white)" stroke="#cfd3dc"/>
    <circle cx="18" cy="18" r="15" fill="var(--white)" stroke="var(--ink)" stroke-width="2"/>
  </svg>

  <div class="contact">
    <p class="contact__name">Corvan Composites PTY LTD</p>
    <p>42 Harbour Rd, Kestrel NSW 2290</p>
    <p>Ph: (02) 5550 1234</p>
    <p>Email: sales@corvancomposites.com.au</p>
    <p>www.corvancomposites.com.au</p>
  </div>
</section>

</body>
</html>
```